Belle Rive Weddings and Events

I am a small boutique wedding coordinator, stylist and bridal consultant/coach/assistant. I am based in Brisbane, Australia and my business is geared towards mid range- high end budget bridal couples.
I am after some business cards that are double sided, with the logo on one side and all other information on the other side, including the business tagline of design, create, celebrate. The look of the card needs to be clean and crisp, with white and the tones of grey of the logo.The final design needs to convey sophistication and poise. Perhaps the logo and tagline could be done in a metallic silver with the rest of the text in the shades of grey from the style guide attached below.
Title- Mira Tolvarenko - Director / Events Manager and Stylist
Address - 218 Halbrook Terrace, Wexley Vale, QLD, 4127
Phone- 07 3894 2167
Mobile- 0438 725 519
Email- Mira@bellerivecelebra.com.au
Website- www.bellerivecelebra.com.au

```html
<!DOCTYPE html>
<html lang="en">
<head>
<meta charset="utf-8">
<title>Belle Rive Weddings and Events – Business Card</title>
<link rel="stylesheet" href="https://fonts.googleapis.com/css2?family=Josefin+Sans:wght@300;400&family=Pinyon+Script&display=swap">
<style>
  :root {
    --backdrop: #e6e6e6;
    --card-white: #ffffff;
    --card-white-tone: #f6f6f6;
    --frame-grey: #7d7d7d;
    --logo-grey: #8a8a8a;
    --card-grey: #8e8e8e;
    --card-grey-tone: #868686;
    --text-light: #ffffff;
    --text-soft: #eeeeee;
  }
  * { margin: 0; padding: 0; box-sizing: border-box; }
  html, body { width: 1200px; height: 900px; overflow: hidden; }
  body {
    background: var(--backdrop);
    font-family: "Josefin Sans", "Helvetica Neue", Arial, sans-serif;
    font-weight: 300;
    position: relative;
  }
  .card {
    position: absolute;
    top: 300px;
    width: 520px;
    height: 300px;
    border-radius: 24px;
    overflow: hidden;
    box-shadow: 0 10px 24px rgba(0,0,0,0.12);
  }
  .card-pattern {
    position: absolute;
    inset: 0;
  }

  /* Front */
  .card-front { left: 50px; background: var(--card-white); }
  .card-front .card-pattern {
    background: radial-gradient(ellipse at center, var(--card-white) 0%, var(--card-white-tone) 100%);
  }
  .front-frame {
    position: absolute;
    inset: 14px;
    border: 5px solid var(--frame-grey);
    border-radius: 16px;
  }
  .brand {
    position: absolute;
    inset: 0;
    display: flex;
    flex-direction: column;
    align-items: center;
    justify-content: center;
    color: var(--logo-grey);
    font-weight: 300;
    text-align: center;
  }
  .brand-name { font-size: 40px; letter-spacing: 1px; line-height: 1.1; }
  .brand-line { font-size: 15px; letter-spacing: 1px; margin-top: 4px; }

  /* Back */
  .card-back { left: 630px; background: var(--card-grey); }
  .card-back .card-pattern {
    background: linear-gradient(135deg, var(--card-grey) 0%, var(--card-grey-tone) 100%);
  }
  .contact {
    position: absolute;
    left: 120px;
    right: 20px;
    top: 42px;
    text-align: center;
    color: var(--text-light);
  }
  .contact-name {
    font-family: "Pinyon Script", cursive;
    font-size: 28px;
    font-weight: 400;
    line-height: 1;
  }
  .contact-title { font-size: 9px; color: var(--text-soft); margin-top: 4px; }
  .contact-phones { margin-top: 24px; font-size: 13px; line-height: 1.5; }
  .contact-web { margin-top: 14px; font-size: 12px; line-height: 1.55; }
  .contact-address { margin-top: 10px; font-size: 12px; }
  .tagline {
    position: absolute;
    left: 28px;
    right: 16px;
    bottom: 32px;
    display: flex;
    justify-content: space-between;
    color: var(--text-light);
    font-size: 9px;
    letter-spacing: 1px;
  }
  .tagline span { display: flex; justify-content: space-between; width: 40%; }
</style>
</head>
<body>

  <section class="card card-front">
    <div class="card-pattern" role="img" aria-label="Faint pale grey floral damask pattern"></div>
    <div class="front-frame"></div>
    <div class="brand">
      <div class="brand-name">Belle Rive</div>
      <div class="brand-line">Weddings &amp; Events</div>
    </div>
  </section>

  <section class="card card-back">
    <div class="card-pattern" role="img" aria-label="Tonal grey floral damask pattern"></div>
    <div class="contact">
      <h1 class="contact-name">Mira Tolvarenko</h1>
      <p class="contact-title">Director / Events Manager and Stylist</p>
      <p class="contact-phones">07 3894 2167<br>0438 725 519</p>
      <p class="contact-web">Mira@bellerivecelebra.com.au<br>www.bellerivecelebra.com.au</p>
      <p class="contact-address">218 Halbrook Terrace, Wexley Vale, QLD, 4127</p>
    </div>
    <p class="tagline" aria-label="Create, Celebrate">
      <span><b>C</b><b>R</b><b>E</b><b>A</b><b>T</b><b>E</b><b>,</b></span>
      <span><b>C</b><b>E</b><b>L</b><b>E</b><b>B</b><b>R</b><b>A</b><b>T</b><b>E</b></span>
    </p>
  </section>

</body>
</html>
```